PHD-project

i need the figures to be in the same stile. info is inside the file. There are 5 figures that need redesign. this is for PhD.

Target Market(s)

it will be used in my phd

Colors

Designer to choose colors to be used in the design.

```html
<!DOCTYPE html>
<html lang="en">
<head>
<meta charset="utf-8">
<title>PhD Project Timeline 2016–2020</title>
<link href="https://fonts.googleapis.com/css2?family=Montserrat:wght@800&family=Roboto:wght@300&display=swap" rel="stylesheet">
<style>
  :root {
    --bg: #ffffff;
    --ink: #222222;
    --year: #ffffff;
    --yellow-a: #f6d816;
    --yellow-b: #e1b20a;
    --orange: #f7960e;
    --green-a: #6fd12a;
    --green-b: #43b41c;
    --blue-a: #0bb8f7;
    --blue-b: #0896e0;
    --purple-a: #9a0ed8;
    --purple-b: #6a02a8;
    --pink-a: #e94fb8;
    --pink-b: #f766c8;
    --icon-light: rgba(255, 255, 255, 0.22);
    --icon-light-line: rgba(255, 255, 255, 0.75);
    --icon-dark: rgba(60, 50, 20, 0.14);
    --icon-dark-line: rgba(60, 50, 20, 0.55);
  }
  html, body {
    margin: 0;
    padding: 0;
    width: 1200px;
    height: 1200px;
    overflow: hidden;
    background: var(--bg);
  }
  .timeline {
    display: block;
    width: 1200px;
    height: 1200px;
  }
  .year {
    font-family: "Montserrat", sans-serif;
    font-weight: 800;
    font-size: 48px;
    fill: var(--year);
    text-anchor: middle;
  }
  .label {
    font-family: "Roboto", sans-serif;
    font-weight: 300;
    font-size: 27px;
    fill: var(--ink);
  }
  .stem { stroke-width: 6; fill: none; }
  .halo { stroke-width: 8; fill: none; }
  .ring { stroke-width: 7; fill: #ffffff; }
  .icon-slot { stroke-width: 3; stroke-dasharray: 8 7; }
  .icon-slot--light { fill: var(--icon-light); stroke: var(--icon-light-line); }
  .icon-slot--dark { fill: var(--icon-dark); stroke: var(--icon-dark-line); }
</style>
</head>
<body>
<svg class="timeline" viewBox="0 0 1500 1500" xmlns="http://www.w3.org/2000/svg" aria-label="Project timeline from 2016 to 2020">
  <defs>
    <linearGradient id="g-yellow" x1="0" x2="1" y1="0" y2="0">
      <stop offset="0" stop-color="var(--yellow-a)"/><stop offset="1" stop-color="var(--yellow-b)"/>
    </linearGradient>
    <linearGradient id="g-green" x1="0" x2="1" y1="0" y2="0">
      <stop offset="0" stop-color="var(--green-a)"/><stop offset="1" stop-color="var(--green-b)"/>
    </linearGradient>
    <linearGradient id="g-blue" x1="0" x2="1" y1="0" y2="0">
      <stop offset="0" stop-color="var(--blue-a)"/><stop offset="1" stop-color="var(--blue-b)"/>
    </linearGradient>
    <linearGradient id="g-purple" x1="1" x2="0" y1="0" y2="0">
      <stop offset="0" stop-color="var(--purple-a)"/><stop offset="1" stop-color="var(--purple-b)"/>
    </linearGradient>
    <linearGradient id="g-pink" x1="0" x2="1" y1="0" y2="0">
      <stop offset="0" stop-color="var(--pink-a)"/><stop offset="1" stop-color="var(--pink-b)"/>
    </linearGradient>
  </defs>

  <!-- stems -->
  <line class="stem" x1="288" y1="788" x2="288" y2="912" stroke="var(--yellow-b)"/>
  <line class="stem" x1="546" y1="596" x2="546" y2="695" stroke="var(--green-b)"/>
  <line class="stem" x1="770" y1="788" x2="770" y2="912" stroke="var(--blue-b)"/>
  <line class="stem" x1="1017" y1="598" x2="1017" y2="695" stroke="var(--purple-b)"/>
  <line class="stem" x1="1279" y1="602" x2="1279" y2="695" stroke="var(--pink-a)"/>

  <!-- chevron band -->
  <g class="band">
    <polygon points="150,678 410,678 447,733 410,788 150,788 190,733" fill="url(#g-yellow)"/>
    <polygon points="410,678 650,678 688,733 650,788 410,788 447,733" fill="url(#g-green)"/>
    <polygon points="650,678 885,678 923,733 885,788 650,788 688,733" fill="url(#g-blue)"/>
    <polygon points="885,678 1120,678 1158,733 1120,788 885,788 923,733" fill="url(#g-purple)"/>
    <polygon points="1120,678 1352,678 1390,733 1352,788 1120,788 1158,733" fill="url(#g-pink)"/>
    <text class="year" x="293" y="761">2016</text>
    <text class="year" x="533" y="761">2017</text>
    <text class="year" x="773" y="761">2018</text>
    <text class="year" x="1013" y="761">2019</text>
    <text class="year" x="1250" y="761">2020</text>
  </g>

  <!-- 2016 marker -->
  <g class="marker">
    <circle class="ring" cx="285" cy="1028" r="117" stroke="var(--yellow-a)"/>
    <circle cx="285" cy="1028" r="102" fill="url(#g-yellow)"/>
    <circle class="icon-slot icon-slot--dark" cx="285" cy="1028" r="68" role="img" aria-label="Icon: a group of students with one raising a hand"/>
    <path class="halo" d="M172,1120 A145,145 0 0 0 398,1120" stroke="var(--orange)"/>
  </g>

  <!-- 2017 marker -->
  <g class="marker">
    <circle class="ring" cx="548" cy="478" r="117" stroke="var(--green-a)"/>
    <circle cx="548" cy="478" r="102" fill="url(#g-green)"/>
    <circle class="icon-slot icon-slot--light" cx="548" cy="478" r="68" role="img" aria-label="Icon: two people talking across a table"/>
    <path class="halo" d="M433,388 A145,145 0 0 1 663,388" stroke="var(--green-b)"/>
  </g>

  <!-- 2018 marker -->
  <g class="marker">
    <circle class="ring" cx="770" cy="1030" r="117" stroke="var(--blue-a)"/>
    <circle cx="770" cy="1030" r="102" fill="url(#g-blue)"/>
    <circle class="icon-slot icon-slot--light" cx="770" cy="1030" r="68" role="img" aria-label="Icon: a person at a screen with a message bubble"/>
    <path class="halo" d="M657,1120 A145,145 0 0 0 885,1120" stroke="var(--blue-b)"/>
  </g>

  <!-- 2019 marker -->
  <g class="marker">
    <circle class="ring" cx="1020" cy="480" r="117" stroke="var(--purple-b)"/>
    <circle cx="1020" cy="480" r="102" fill="url(#g-purple)"/>
    <circle class="icon-slot icon-slot--light" cx="1020" cy="480" r="68" role="img" aria-label="Icon: an interview panel at a table"/>
    <path class="halo" d="M905,390 A145,145 0 0 1 1135,390" stroke="var(--purple-b)"/>
  </g>

  <!-- 2020 marker -->
  <g class="marker">
    <circle class="ring" cx="1293" cy="483" r="117" stroke="var(--pink-a)"/>
    <circle cx="1293" cy="483" r="102" fill="url(#g-pink)"/>
    <circle class="icon-slot icon-slot--light" cx="1293" cy="483" r="68" role="img" aria-label="Icon: a checklist with a thumbs up"/>
    <path class="halo" d="M1178,393 A145,145 0 0 1 1408,393" stroke="var(--pink-b)"/>
  </g>

  <!-- labels -->
  <text class="label" x="205" y="568">
    <tspan x="205">Prequel with</tspan>
    <tspan x="205" dy="35">student-led</tspan>
    <tspan x="205" dy="35">innovation</tspan>
  </text>
  <text class="label" x="705" y="630">Interventions</text>
  <text class="label" x="460" y="852">
    <tspan x="460">First Round of</tspan>
    <tspan x="460" dy="35">interviews</tspan>
  </text>
  <text class="label" x="945" y="845">
    <tspan x="945">Second</tspan>
    <tspan x="945" dy="35">Round of</tspan>
    <tspan x="945" dy="35">interviews</tspan>
  </text>
  <text class="label" x="1193" y="845">
    <tspan x="1193">Additional</tspan>
    <tspan x="1193" dy="35">interviews and</tspan>
    <tspan x="1193" dy="35">comments</tspan>
  </text>
</svg>
</body>
</html>
```